Redesign business cards

We have a new logo and I am not that happy with the layout of our existing card and looking for a change. Font is a bit small and the green can be hard to read. Logo may need a tidy up as the copy I have is not that hi-res too so require you to produce a hi-res version of the logo for us too. There will be three individual business cards to produce with just the names and phone numbers being different. Address will change too, but use what you see on the card for now.

Industry/Entity Type

Business

Requirements
Nice to have
• You could consider a redesign to the new logo, just not too radical. We like the blue and green hexagons as we feel that they are representative of oil industry that we are in.

```html
<!DOCTYPE html>
<html lang="en">
<head>
<meta charset="utf-8">
<title>Hexaline Fluid Services – Business Card</title>
<link href="https://fonts.googleapis.com/css2?family=Arimo:ital,wght@0,400;0,700;1,400&display=swap" rel="stylesheet">
<style>
  :root {
    --bg: #d9d9d7;
    --card-white: #f7f7f5;
    --brand-blue: #1a8fcb;
    --brand-blue-light: #4fb3e3;
    --brand-green: #78b234;
    --ink: #1d1d1d;
    --ink-soft: #555555;
    --grey: #8a8a8a;
    --icon-blue: #2288c6;
  }
  * { box-sizing: border-box; margin: 0; padding: 0; }
  html, body { width: 1200px; height: 1000px; overflow: hidden; }
  body {
    background: var(--bg);
    font-family: "Arimo", Arial, sans-serif;
    position: relative;
  }
  .card {
    position: absolute;
    left: 270px;
    width: 660px;
    height: 400px;
    border-radius: 4px;
    box-shadow: 0 6px 18px rgba(0,0,0,0.18);
    overflow: hidden;
  }
  /* Back of card */
  .card--back {
    top: 45px;
    background: var(--brand-blue);
    display: flex;
    flex-direction: column;
    align-items: center;
    justify-content: center;
    gap: 34px;
  }
  .wordmark {
    display: flex;
    align-items: center;
    gap: 16px;
  }
  .wordmark__dot {
    width: 22px;
    height: 22px;
    border-radius: 50%;
    background: var(--brand-green);
    flex: none;
  }
  .wordmark__name {
    font-family: "Arimo", Arial, sans-serif;
    font-weight: 700;
    font-size: 48px;
    line-height: 1;
    color: #ffffff;
  }
  .card--back .website {
    font-size: 22px;
    letter-spacing: 0.32em;
    color: rgba(255,255,255,0.72);
  }
  /* Front of card */
  .card--front {
    top: 495px;
    background: var(--card-white);
  }
  .card--front .wordmark {
    position: absolute;
    left: 44px;
    top: 52px;
  }
  .card--front .wordmark__name {
    font-size: 40px;
    color: var(--brand-blue);
  }
  .card--front .wordmark__dot { background: var(--brand-green); }
  .card__pattern {
    position: absolute;
    right: 0;
    top: 110px;
    width: 260px;
    height: 290px;
    background: linear-gradient(160deg, rgba(79,179,227,0) 20%, rgba(79,179,227,0.35) 60%, rgba(34,136,198,0.7) 100%);
  }
  .contact {
    position: absolute;
    left: 300px;
    top: 158px;
    color: var(--ink);
  }
  .contact__name {
    font-weight: 700;
    font-size: 19px;
    color: var(--icon-blue);
  }
  .contact__cred {
    font-weight: 400;
    font-size: 14px;
    color: var(--grey);
    margin-left: 8px;
  }
  .contact__role {
    font-style: italic;
    font-size: 14px;
    color: var(--ink-soft);
    margin-top: 3px;
    margin-bottom: 14px;
  }
  .contact__list { list-style: none; }
  .contact__item {
    display: flex;
    align-items: center;
    gap: 9px;
    font-size: 19px;
    line-height: 27px;
  }
  .contact__icon { width: 17px; height: 17px; flex: none; }
  .contact__item b { font-weight: 700; }
  .address {
    font-style: normal;
    font-size: 19px;
    line-height: 23px;
    margin-top: 10px;
  }
</style>
</head>
<body>

<section class="card card--back" aria-label="Card back">
  <div class="wordmark">
    <span class="wordmark__name">Hexaline Fluid Services</span>
    <span class="wordmark__dot" aria-hidden="true"></span>
  </div>
  <p class="website">www.hexaline.com.au</p>
</section>

<section class="card card--front" aria-label="Card front">
  <div class="wordmark">
    <span class="wordmark__name">Hexaline Fluid Services</span>
    <span class="wordmark__dot" aria-hidden="true"></span>
  </div>

  <div class="card__pattern" role="img" aria-label="Decorative curved line pattern in light blue"></div>

  <div class="contact">
    <p class="contact__name">Daniel Whitford<span class="contact__cred">NZCE (Mech) P&amp;P</span></p>
    <p class="contact__role">Director</p>
    <ul class="contact__list">
      <li class="contact__item">
        <svg class="contact__icon" viewBox="0 0 16 16" aria-hidden="true">
          <rect width="16" height="16" rx="3" fill="var(--icon-blue)"/>
          <path d="M5 3.5 L6.8 5.6 L5.9 6.8 Q7 9 9.2 10.1 L10.4 9.2 L12.5 11 L11.4 12.5 Q7.5 12.4 4.5 8.5 Q3.4 6 3.8 4.4 Z" fill="#fff"/>
        </svg>
        +614 555 01842
      </li>
      <li class="contact__item">
        <svg class="contact__icon" viewBox="0 0 16 16" aria-hidden="true">
          <rect width="16" height="16" rx="3" fill="var(--icon-blue)"/>
          <rect x="3" y="4.5" width="10" height="7" fill="none" stroke="#fff" stroke-width="1.2"/>
          <path d="M3 4.5 L8 8.5 L13 4.5" fill="none" stroke="#fff" stroke-width="1.2"/>
        </svg>
        daniel@hexalinefluid.co.nz
      </li>
      <li class="contact__item">
        <svg class="contact__icon" viewBox="0 0 16 16" aria-hidden="true">
          <rect width="16" height="16" rx="3" fill="var(--icon-blue)"/>
          <circle cx="8" cy="8" r="4.8" fill="none" stroke="#fff" stroke-width="1.1"/>
          <ellipse cx="8" cy="8" rx="2" ry="4.8" fill="none" stroke="#fff" stroke-width="1"/>
          <path d="M3.2 8 H12.8" stroke="#fff" stroke-width="1"/>
        </svg>
        <span>www.<b>hexaline</b>.com.au</span>
      </li>
    </ul>
    <address class="address">
      Unit 214/560 Harbour Rd<br>
      Kingsford Bay<br>
      Queensland 4199
    </address>
  </div>
</section>

</body>
</html>
```